Web development startup company needs a web design

We need a design for a company starting out, based in Australia. The business focuses on Quarvo database solutions - Quarvo database development, web development, support, etc. As such, needs a professional look and feel to it.
I'm thinking a single page design where the user can either click a nav bar to go to the relevant section in the page or scroll down is the best shot - but I'm no designer so happy with any suggestions.
I envisions three sections to the page
1. An about us:
2. Project listing
3. Contact form.
Industry/Entity Type
Business
Coding
Coded - Design and coding required
Number of Pages Required
1 page
Look and feel

```html
<!DOCTYPE html>
<html lang="en">
<head>
<meta charset="utf-8">
<title>Shoreline Data Solutions</title>
<link href="https://fonts.googleapis.com/css2?family=Roboto:wght@300;400;500&family=Open+Sans:ital,wght@0,400;0,600;1,400&display=swap" rel="stylesheet">
<style>
:root{
  --accent:#23b5e3;
  --accent-dark:#1a9dc8;
  --ink:#222;
  --body:#666;
  --muted:#888;
  --line:#ddd;
  --white:#fff;
  --grey-band:#ebebeb;
  --light-band:#f5f5f5;
  --footer-dark:#151a1d;
  --social:#1d6a88;
}
*{margin:0;padding:0;box-sizing:border-box}
html,body{width:1200px;height:2707px;overflow:hidden}
body{position:relative;font-family:"Open Sans",Arial,sans-serif;color:var(--body);background:var(--white)}
.section-title{position:absolute;left:0;width:1200px;text-align:center;font-family:"Roboto",Arial,sans-serif;font-weight:400;font-size:33px;color:var(--ink);letter-spacing:.5px}

/* Hero */
.hero{position:absolute;left:0;top:0;width:1200px;height:650px;overflow:hidden}
.hero-photo{position:absolute;inset:0;background:
  radial-gradient(ellipse at 70% 35%,rgba(120,220,235,.55),transparent 55%),
  radial-gradient(ellipse at 30% 70%,rgba(200,170,150,.45),transparent 50%),
  linear-gradient(180deg,#0e2a33 0%,#2a6f7d 40%,#7bb6c0 70%,#c9d4d6 100%)}
.topbar{position:absolute;left:0;top:0;width:1200px;height:108px;background:linear-gradient(180deg,rgba(0,0,0,.75),rgba(0,0,0,.35))}
.brand{position:absolute;left:112px;top:34px;display:flex;align-items:center;gap:12px}
.brand-mark{width:38px;height:38px;border-radius:50%;background:var(--accent)}
.brand-name{font-family:"Roboto",Arial,sans-serif;font-weight:500;font-size:25px;color:var(--accent)}
.nav{position:absolute;top:38px;left:588px;display:flex;font-size:13px;font-weight:600;color:var(--white);letter-spacing:.3px}
.nav a{color:var(--white);text-decoration:none;display:block;height:34px;line-height:32px}
.nav .home{width:72px;text-align:center;border:2px solid var(--accent);border-radius:3px;color:var(--accent)}
.hero-caption{position:absolute;left:0;top:455px;width:1200px;height:115px;background:rgba(70,80,85,.55);color:var(--white);font-family:"Roboto",Arial,sans-serif;font-weight:400;font-size:30px;text-align:center;line-height:115px;letter-spacing:.5px}
.dots{position:absolute;top:609px;left:553px;display:flex;gap:12px}
.dots span{width:14px;height:14px;border-radius:50%;background:#b9b9b9}
.dots .on{background:var(--accent)}

/* About */
.about{position:absolute;left:0;top:650px;width:1200px;height:425px}
.about-text{position:absolute;left:112px;top:82px;width:976px;text-align:center;font-size:12.5px;line-height:31.5px;color:var(--body)}
.service{position:absolute;top:208px;width:250px;text-align:center}
.service-icon{margin:0 auto;width:72px;height:72px;border-radius:50%;background:var(--accent);position:relative;box-shadow:-14px 8px 14px rgba(0,0,0,.12)}
.service-icon svg{position:absolute;left:22px;top:22px}
.service h3{margin-top:26px;font-family:"Roboto",Arial,sans-serif;font-weight:400;font-size:14px;color:var(--ink);letter-spacing:.1px;white-space:nowrap}
.service p{margin:10px auto 0;width:230px;font-size:11.5px;line-height:24px;color:var(--body)}

/* Projects */
.projects{position:absolute;left:0;top:1075px;width:1200px;height:425px;background:var(--grey-band)}
.project{position:absolute;top:93px;width:224px;height:290px;background:var(--white);overflow:hidden}
.project-image{width:224px;height:146px}
.project h3{margin:17px 16px 0;font-family:"Roboto",Arial,sans-serif;font-weight:400;font-size:13px;color:var(--ink);line-height:20px}
.project p{margin:5px 16px 0;font-size:11px;line-height:20px;color:var(--body)}

/* Blog */
.blog{position:absolute;left:0;top:1500px;width:1200px;height:261px}
.post{position:absolute;top:101px;height:128px}
.post-image{position:absolute;left:0;top:0;width:202px;height:128px;border-bottom:3px solid var(--accent)}
.post-body{position:absolute;left:220px;top:-3px;width:254px}
.post-date{font-size:10.5px;font-style:italic;color:var(--accent)}
.post h3{margin-top:4px;font-family:"Roboto",Arial,sans-serif;font-weight:400;font-size:14px;line-height:21px;color:var(--ink)}
.post-rule{margin-top:8px;height:1px;background:var(--line);position:relative}
.post-rule::before{content:"";position:absolute;left:0;top:0;width:60px;height:1px;background:var(--accent)}
.post p{margin-top:10px;font-size:11.5px;line-height:21.5px;color:var(--body)}

/* Contact */
.contact{position:absolute;left:0;top:1761px;width:1200px;height:459px;background:var(--light-band)}
.contact-lead{position:absolute;left:0;top:80px;width:1200px;text-align:center;font-size:11.5px;color:var(--body)}
.field{position:absolute;left:112px;width:474px;height:52px;background:var(--white);border:1px solid var(--line);font-size:10.5px;color:var(--muted);padding:18px 18px}
.field.message{left:614px;top:127px;width:472px;height:205px}
.send{position:absolute;left:529px;top:366px;width:142px;height:51px;background:var(--accent);color:var(--white);font-size:11.5px;font-weight:600;text-align:center;line-height:51px;border-radius:2px;letter-spacing:.3px}

/* Keep in touch */
.touch{position:absolute;left:0;top:2220px;width:1200px;height:404px;overflow:hidden}
.touch-photo{position:absolute;inset:0;background:
  linear-gradient(180deg,rgba(45,180,225,.88),rgba(45,180,225,.9)),
  linear-gradient(90deg,#2a7fa0,#6fd0ef 50%,#2a7fa0)}
.touch-panel{position:absolute;left:336px;top:50px;width:527px;height:300px;background:rgba(255,255,255,.14)}
.touch-title{position:absolute;left:0;top:42px;width:527px;text-align:center;font-family:"Roboto",Arial,sans-serif;font-weight:400;font-size:31px;color:var(--white);letter-spacing:.5px}
.info{position:absolute;display:flex;align-items:center;gap:14px;font-family:"Roboto",Arial,sans-serif;font-size:16px;color:var(--white);white-space:nowrap}
.info-icon{width:40px;height:40px;border-radius:50%;background:var(--white);display:flex;align-items:center;justify-content:center}
.socials{position:absolute;left:157px;top:243px;display:flex;gap:7px}
.socials span{width:36px;height:36px;border-radius:50%;background:var(--social);display:flex;align-items:center;justify-content:center}
.socials .share{background:#189a5a}

/* Footer */
.footer{position:absolute;left:0;top:2624px;width:1200px;height:83px;background:var(--footer-dark);font-size:11.5px;color:#8a8f92}
.footer .copy{position:absolute;left:112px;top:32px}
.footer .legal{position:absolute;right:112px;top:32px}
</style>
</head>
<body>

<header class="hero">
  <div class="hero-photo" role="img" aria-label="Photo of hands typing on a keyboard overlaid with glowing business charts, a world map and binary digits"></div>
  <div class="topbar"></div>
  <div class="brand"><span class="brand-mark"></span><span class="brand-name">Shoreline Data Solutions</span></div>
  <nav class="nav">
    <a class="home" href="#">HOME</a>
    <a href="#" style="margin-left:38px">ABOUT US</a>
    <a href="#" style="margin-left:46px">PROJECTS</a>
    <a href="#" style="margin-left:46px">BLOG</a>
    <a href="#" style="margin-left:46px">CONTACT US</a>
  </nav>
  <div class="hero-caption">QUARVO DATABASE DEVELOPMENT BUSINESS</div>
  <div class="dots"><span></span><span class="on"></span><span></span><span></span></div>
</header>

<section class="about">
  <h2 class="section-title" style="top:38px">ABOUT US</h2>
  <p class="about-text">We are an Quarvo Database Development business specialising in tailormade solutions.Our focus is with Rapid Builder, an Quarvo rapid web application development framework. Some of our project highlights include integrating with Vantix APIs Drive,Calendar just to name a couple. If you have Quarvo database in your organisation and need additional resources, don't hesitate to contact us for a quote.</p>

  <div class="service" style="left:99px">
    <div class="service-icon"><svg width="28" height="28" viewBox="0 0 28 28" fill="none" stroke="#fff" stroke-width="2"><path d="M14 4a7 7 0 0 0-4 12.7V20h8v-3.3A7 7 0 0 0 14 4z"/><path d="M11 23h6"/></svg></div>
    <h3>QUARVO DATABASE SOLUTIONS</h3>
    <p>Lorem ipsum dolor sit amet, consectetuer adipiscing elit, sed diam nonummy nibh euismod tincidunt ut laoreet.</p>
  </div>
  <div class="service" style="left:348px">
    <div class="service-icon"><svg width="28" height="28" viewBox="0 0 28 28"><path fill="#fff" d="M8 21a5 5 0 0 1-.6-10A7 7 0 0 1 21 12a4.5 4.5 0 0 1 0 9z"/></svg></div>
    <h3>QUARVO DATABASE DEVELOPMENT</h3>
    <p>Ut wisi enim ad minim veniam, quis no strud exerci tation ullamcorper suscipit lobortis nisl ut aliquip.</p>
  </div>
  <div class="service" style="left:599px">
    <div class="service-icon"><svg width="28" height="28" viewBox="0 0 28 28" fill="none" stroke="#fff" stroke-width="2.2"><rect x="4" y="6" width="20" height="13" rx="1"/><path d="M11 24h6M14 19v5"/></svg></div>
    <h3>WEB DEVELOPMENT</h3>
    <p>Lorem ipsum dolor sit amet, consectetuer adipiscing elit, sed diam nonummy nibh euismod tincidunt ut laoreet.</p>
  </div>
  <div class="service" style="left:849px">
    <div class="service-icon"><svg width="28" height="28" viewBox="0 0 28 28" fill="none" stroke="#fff" stroke-width="2.2"><circle cx="14" cy="14" r="9"/><circle cx="14" cy="14" r="4"/><path d="M8 8l3 3M20 8l-3 3M8 20l3-3M20 20l-3-3"/></svg></div>
    <h3>WEB SUPPORT</h3>
    <p>Ut wisi enim ad minim veniam, quis no strud exerci tation ullamcorper suscipit lobortis nisl ut aliquip.</p>
  </div>
</section>

<section class="projects">
  <h2 class="section-title" style="top:38px">OUR PROJECTS</h2>
  <article class="project" style="left:112px">
    <div class="project-image" role="img" aria-label="Photo of a fanned stack of black printed cards" style="background:linear-gradient(135deg,#f2f2f2,#2a2a2a 55%,#0d0d0d)"></div>
    <h3>CARD PRINTING SYSTEM</h3>
    <p>Managing staff accounts and printing off cards, technologies used; JavaScript, QL/SQL, SQL, jLite, Rapid Builder</p>
  </article>
  <article class="project" style="left:362px">
    <div class="project-image" role="img" aria-label="Photo of a gloved hand pipetting into a red laboratory sample tray" style="background:linear-gradient(160deg,#e8ecef 0%,#cfd6db 45%,#e23a4a 75%,#c91e33 100%)"></div>
    <h3>RESEARCH SYSTEM</h3>
    <p>Build an ETL script to migrate data from TableCore Server that runs on a frequent basis, loaded into Quarvo, and build reports on the data.</p>
  </article>
  <article class="project" style="left:613px">
    <div class="project-image" role="img" aria-label="Illustration of a white cloud with device icons on a blue sky" style="background:radial-gradient(ellipse at 50% 50%,#e6f4ff 0%,#6fb4ea 35%,#1f6fc2 100%)"></div>
    <h3>CLOUD STORAGE INTEGRATION</h3>
    <p>Building forms to upload data to various cloud hosting providers such as Nimbus Vault, Vantix Drive.</p>
  </article>
  <article class="project" style="left:864px">
    <div class="project-image" role="img" aria-label="Illustration of blue cloud shapes with server stacks over a teal sky" style="background:linear-gradient(135deg,#dfe6e9 0%,#6aa9c6 40%,#1f6fae 70%,#2aa0b8 100%)"></div>
    <h3>WIKIFLOW DOCUMENT LIBRARY</h3>
    <p>Interfacing with Kestrel Wikiflow wiki using their SOAP API to store revisions in an Quarvo database.</p>
  </article>
</section>

<section class="blog">
  <h2 class="section-title" style="top:38px">BLOG</h2>
  <article class="post" style="left:112px">
    <div class="post-image" role="img" aria-label="Illustration of blue clouds connected to computers and mobile devices" style="background:linear-gradient(180deg,#f4f6f8,#dfe5ea)"></div>
    <div class="post-body">
      <div class="post-date">March 23, 2015</div>
      <h3>Lorem ipsum dolor sit amet, conse cte tuer adipiscing elit</h3>
      <div class="post-rule"></div>
      <p>Ut wisi enim ad minim veniam, quis nostrud exerci tation ullamcorper suscipit lobortis nisl ut aliquip ex ea commodo consequat.</p>
    </div>
  </article>
  <article class="post" style="left:614px">
    <div class="post-image" role="img" aria-label="Illustration of a yellow folder under a blue cloud on a glowing green background" style="background:radial-gradient(ellipse at 45% 55%,#c9e84a 0%,#4a9a2a 45%,#123d18 100%)"></div>
    <div class="post-body">
      <div class="post-date">March 23, 2015</div>
      <h3>Duis autem vel eum iriure dolor in hen dreit in vulputate velit esse molestie</h3>
      <div class="post-rule"></div>
      <p>Ut wisi enim ad minim veniam, quis nostrud exerci tation ullamcorper suscipit lobortis nisl ut aliquip ex ea commodo consequat.</p>
    </div>
  </article>
</section>

<section class="contact">
  <h2 class="section-title" style="top:28px">CONTAC US</h2>
  <p class="contact-lead">Lorem ipsum dolor sit amet, consectetuer adipiscing elit, sed diam nonummy nibh euismod tincidunt ut laoreet dolore magna aliquam erat volutpat.</p>
  <div class="field" style="top:127px">Name</div>
  <div class="field" style="top:204px">Email Address</div>
  <div class="field" style="top:281px">Phone</div>
  <div class="field message">Message</div>
  <div class="send">SEND MAIL</div>
</section>

<section class="touch">
  <div class="touch-photo" role="img" aria-label="Aerial photo of a city skyline tinted bright blue"></div>
  <div class="touch-panel">
    <h2 class="touch-title">KEEP IN TOUCH</h2>
    <div class="info" style="left:43px;top:103px">
      <span class="info-icon"><svg width="16" height="18" viewBox="0 0 16 18"><rect x="4" y="1" width="8" height="16" rx="1.5" fill="none" stroke="#23b5e3" stroke-width="1.8"/><circle cx="8" cy="14" r="1" fill="#23b5e3"/></svg></span>1-5550-321-900
    </div>
    <div class="info" style="left:230px;top:103px">
      <span class="info-icon"><svg width="18" height="14" viewBox="0 0 18 14"><rect x="1" y="1" width="16" height="12" rx="1" fill="#23b5e3"/><path d="M1 2l8 6 8-6" fill="none" stroke="#fff" stroke-width="1.4"/></svg></span>info@shorelinedata.example
    </div>
    <div class="info" style="left:43px;top:164px">
      <span class="info-icon"><svg width="14" height="18" viewBox="0 0 14 18"><path d="M7 1a6 6 0 0 0-6 6c0 4.5 6 10 6 10s6-5.5 6-10a6 6 0 0 0-6-6z" fill="#23b5e3"/><circle cx="7" cy="7" r="2.2" fill="#fff"/></svg></span>2 Lorem Ipsm , Lorem Ipsm, loremIpsm - 123 456
    </div>
    <div class="socials">
      <span></span><span></span><span></span><span></span><span></span>
      <span class="share"><svg width="18" height="18" viewBox="0 0 18 18" fill="#fff"><circle cx="13" cy="4" r="2.5"/><circle cx="5" cy="9" r="2.5"/><circle cx="13" cy="14" r="2.5"/><path d="M5 9l8-5M5 9l8 5" stroke="#fff" stroke-width="1.5"/></svg></span>
    </div>
  </div>
</section>

<footer class="footer">
  <span class="copy">Copyrights @ 2014 Shoreline Data Solutions. All Right Reserved.</span>
  <span class="legal">Privacy Statement | Terms &amp; Conditions</span>
</footer>

</body>
</html>
```